Tandra Link and recovery web and app design

GPS enabled APP providing breakdown and assistance for cyclists by cyclists.
24 hour bicycle assist and recovery package for both road and off road cyclists.
First and only bicycle assist package whose aim is to get you back on your bike to complete your journey

I need the design package to give a website designer so they can build website and app. I have a logo done by my nephew which is the company logo but i need a full design package now.

Below is the website banner I have now and the logo
Updates

Reason: I am moving house today and have no internet till Tuesday so please extend deadline 5 days to allow everyone

Target Market(s)

Cyclists in the South East and London, and then all UK, includes MTB off road and road cyclists. Please see farrowspinline.co.uk as this was my pretotype website for market information.

Number of Pages Required

5+ page

Font styles to use
Other font styles liked:
• FARROW SPINLINE

Colors
ffcf3e
f04b51
f68d4c
faa54b
fbee3f
add136

Requirements
Must have
• Landing page, mechanical page, medical page, FAQ page, policy information page accessible by policy holder to update, lost password page, quote page, pay page, contact us page, all policy info must be accessible by Norvane Desk out operations room provider,
Nice to have
• Lots of great action cycling photos and very usable website

```html
<!DOCTYPE html>
<html lang="en">
<head>
<meta charset="utf-8">
<title>Tandra Link UK – Mechanic Registration</title>
<link href="https://fonts.googleapis.com/css2?family=Open+Sans:wght@400;600&family=Roboto:wght@400;500&display=swap" rel="stylesheet">
<style>
  :root {
    --header-bg: #201e1c;
    --footer-bg: #2c2a29;
    --page-bg: #eedcdf;
    --page-bg-2: #e7d2d6;
    --panel-bg: #ffffff;
    --panel-band: #f2f2f2;
    --panel-border: #d9d0d2;
    --brand-red: #e93c44;
    --brand-red-dark: #c92a32;
    --accent-orange: #f67b2f;
    --field-bg: #f9f9f9;
    --field-border: #e6e6e6;
    --text: #333333;
    --text-muted: #666666;
    --text-soft: #888888;
    --nav-text: #ffffff;
    --logo-text: #d9d9d9;
  }
  * { box-sizing: border-box; margin: 0; padding: 0; }
  html, body { width: 1200px; height: 1168px; overflow: hidden; }
  body {
    font-family: "Open Sans", sans-serif;
    color: var(--text);
    background: linear-gradient(135deg, var(--page-bg) 0%, var(--page-bg-2) 50%, var(--page-bg) 100%);
    position: relative;
  }

  .site-header {
    height: 99px;
    background: var(--header-bg);
    position: relative;
  }
  .brand {
    position: absolute; left: 84px; top: 22px;
    display: flex; align-items: center; gap: 14px;
  }
  .brand-dot { width: 44px; height: 44px; border-radius: 50%; background: var(--brand-red); }
  .brand-name {
    font-family: "Roboto", sans-serif; font-weight: 500;
    font-size: 31px; letter-spacing: 0.5px; color: var(--logo-text);
    border-top: 1px solid #666; border-bottom: 1px solid #666;
    padding: 4px 0;
  }
  .main-nav {
    position: absolute; right: 99px; top: 29px;
    display: flex; align-items: center;
    font-family: "Roboto", sans-serif; font-size: 13.5px;
  }
  .main-nav a { color: var(--nav-text); text-decoration: none; margin-left: 39px; }
  .main-nav a:first-child { margin-left: 0; }
  .main-nav .btn-signup {
    background: var(--accent-orange); padding: 8px 12px; border-radius: 3px; margin-left: 34px;
  }

  .panel {
    position: absolute; left: 99px; top: 131px; width: 1003px; height: 964px;
    background: var(--panel-bg); border: 1px solid var(--panel-border);
  }
  .panel-head {
    height: 63px; background: linear-gradient(#ffffff, #ececec);
    display: flex; align-items: center; justify-content: center; gap: 12px;
    font-family: "Roboto", sans-serif; font-size: 20px; color: var(--text);
  }
  .panel-head .mark { width: 12px; height: 12px; border-radius: 50%; background: var(--brand-red); }

  .intro { text-align: center; padding-top: 30px; }
  .intro .mark { width: 60px; height: 60px; border-radius: 50%; background: var(--brand-red); margin: 0 auto; }
  .intro h2 {
    font-family: "Roboto", sans-serif; font-weight: 400;
    color: var(--brand-red); font-size: 21px; margin-top: 23px;
  }
  .intro p { font-size: 11.5px; line-height: 21px; color: var(--text-muted); margin: 6px auto 0; width: 420px; }
  .divider {
    position: absolute; left: 210px; top: 273px; width: 580px; height: 1px;
    background: linear-gradient(90deg, transparent, #e4e4e4, transparent);
  }

  .form-row { position: absolute; left: 277px; display: flex; align-items: center; }
  .form-row label { width: 130px; font-size: 11.5px; color: var(--text); }
  .field {
    width: 317px; height: 38px; background: var(--field-bg); border: 1px solid var(--field-border);
  }
  .date-group { display: flex; gap: 8px; }
  .date-field {
    width: 100px; height: 37px; background: #fff; border: 1px solid var(--field-border);
    display: flex; align-items: center; justify-content: space-between;
    font-size: 15px; color: var(--text-soft); padding-left: 13px;
  }
  .spin { width: 33px; height: 100%; border-left: 1px solid var(--field-border); display: flex; align-items: center; justify-content: center; }

  .desc-label { position: absolute; left: 276px; top: 627px; font-size: 11.5px; }
  .desc-field {
    position: absolute; left: 277px; top: 654px; width: 448px; height: 109px;
    background: var(--field-bg); border: 1px solid var(--field-border);
  }
  .signature { position: absolute; top: 817px; width: 159px; border-top: 1px solid #ddd; padding-top: 6px; font-size: 14.5px; color: var(--text-soft); }

  .panel-foot {
    position: absolute; left: 0; bottom: 0; width: 100%; height: 72px; background: var(--panel-band);
    display: flex; align-items: center; justify-content: center;
  }
  .btn-primary {
    width: 214px; height: 40px; background: var(--brand-red); border-bottom: 2px solid var(--brand-red-dark);
    border-radius: 3px; color: #fff; font-family: "Roboto", sans-serif; font-weight: 500; font-size: 15px;
    display: flex; align-items: center; justify-content: center;
  }

  .site-footer {
    position: absolute; left: 0; top: 1114px; width: 1200px; height: 54px; background: var(--footer-bg);
    display: flex; align-items: center; justify-content: center; font-size: 12.5px; color: #e6e6e6;
  }
</style>
</head>
<body>
  <header class="site-header">
    <div class="brand">
      <span class="brand-dot"></span>
      <span class="brand-name">TANDRA LINK UK</span>
    </div>
    <nav class="main-nav">
      <a href="#">HOME</a>
      <a href="#">PACKAGE</a>
      <a href="#">MOBILE APPS</a>
      <a href="#">CONTACT</a>
      <a href="#" class="btn-signup">SIGN UP</a>
    </nav>
  </header>

  <main class="panel">
    <div class="panel-head"><span class="mark"></span>MECHANIC REGISTRATION</div>
    <div class="intro">
      <div class="mark"></div>
      <h2>MECHANIC CONTRACT SIGNED</h2>
      <p>Sed ut perspiciatis unde omnis iste natus error sit voluptatem accusantium doloremque laudantium, totam rem aperiam, eaque</p>
    </div>
    <div class="divider"></div>

    <div class="form-row" style="top:308px"><label>Mechanic Name :</label><div class="field"></div></div>
    <div class="form-row" style="top:359px"><label>Email Address :</label><div class="field"></div></div>
    <div class="form-row" style="top:411px"><label>The Lienholder :</label><div class="field"></div></div>
    <div class="form-row" style="top:462px"><label>Located at :</label><div class="field"></div></div>
    <div class="form-row" style="top:513px"><label>Provided Materals to :</label><div class="field"></div></div>
    <div class="form-row" style="top:564px; left:276px"><label style="width:131px">Agreement Dated :</label>
      <div class="date-group">
        <div class="date-field">dd<span class="spin"><svg width="10" height="16" viewBox="0 0 10 16" fill="none" stroke="#777" stroke-width="1.3"><path d="M2 5l3-3 3 3M2 11l3 3 3-3"/></svg></span></div>
        <div class="date-field">mm<span class="spin"><svg width="10" height="16" viewBox="0 0 10 16" fill="none" stroke="#777" stroke-width="1.3"><path d="M2 5l3-3 3 3M2 11l3 3 3-3"/></svg></span></div>
        <div class="date-field">yyyy<span class="spin"><svg width="10" height="16" viewBox="0 0 10 16" fill="none" stroke="#777" stroke-width="1.3"><path d="M2 5l3-3 3 3M2 11l3 3 3-3"/></svg></span></div>
      </div>
    </div>

    <div class="desc-label">Work done description :</div>
    <div class="desc-field"></div>

    <div class="signature" style="left:278px">Your signed</div>
    <div class="signature" style="left:561px">contract signed</div>

    <div class="panel-foot"><div class="btn-primary">MECHANIC REGISTRATION</div></div>
  </main>

  <footer class="site-footer">Copyright © Tandra Link UK. All rights reserved. Contact Us / T&amp;Cs / Privacy Policy</footer>
</body>
</html>
```